Ticket Website Design

The project is to design a website for a ticket business. We sell ticket for sports, theater and concerts.

- Below are some ticket design styles that we like -

PassHarbor.com
BrightRowz.com
GateNook.com
AdmitPlacing.com
Plov.com
FlenTrek.com

- Homepage features -

The main navigation should be the following links:
Upcoming, Sports, Concerts, Theater, Las Vegas, Location, Other

The main navigation should have a drop down menu designed.

The homepage should have a featured search box that is in a location that can be carried through to an internal page.

The site should be around 1000px width

We don't have a logo yet so you can use a placeholder in the logo location. I'll work to upload a placeholder logo if a designer don't have one.

We’d like to keep the background of the site lighter and not a dark solid background

You are free to do colors to your liking. However, please make them good combination colors and nothing that is very bright (i.e. Lime green). Some possible example colors would be “black/red”, “blue/orange”

We'd like the logo in the top left of the site.

- Other homepage elements -

Featured Events (Slider Box with Image)
Events In the Next 60 Days (Listing)
Newsletter (Form)
Buyer Guarantee (Design Box)
Testimonials (2 Featured Testimonials)
Featured Sports Tickets (Heading/Listing)
Featured Concert Tickets (Heading/Listing)
Featured Theater Tickets (Heading/Listing)
Featured Tickets By City (Heading/Listing)
Featured Phone Number / Less Featured International Number
Social Icons
“Your Location” See PassHarbor.com in the header. This shows the location of the visitor and features events in their area. They can click a small button to edit that location.

- What we are looking for overall -

We are looking for a high quality professional homepage design that contains all of the homepage features listed. While you are designing the homepage, please keep in mind the transition to an internal page. We want it to be a smooth transition. For example: if there is a column on the homepage, that column follows through on the internal page.

If you have some thoughts or questions on that let me know and I’d be happy to answer before you design.
Updates

Project Deadline Extended
Reason: A few designers asked for a few more days to submit their designs. Thanks for understanding. Let me know if anyone has any questions. Thanks, Dorn

Target Market(s)

18-35

Industry/Entity Type

Events

Requirements
Should not have
• No really bright colors (lime green/pink, etc.)

```html
<!DOCTYPE html>
<html lang="en">
<head>
<meta charset="utf-8">
<title>SeatLoft – Tickets for Sports, Theater and Concerts</title>
<link href="https://fonts.googleapis.com/css2?family=Bree+Serif&family=Bitter:wght@400;700&display=swap" rel="stylesheet">
<style>
:root{
  --red:#d9181b;
  --red-dark:#a90d10;
  --gold:#fcc13b;
  --gold-dark:#e9a416;
  --ink:#333;
  --muted:#777;
  --line:#dcdcdc;
  --cream:#fde9b3;
  --page:#fff;
}
*{box-sizing:border-box;margin:0;padding:0}
html,body{width:738px;height:1200px;overflow:hidden;background:var(--page)}
body{font-family:"Bitter",Georgia,serif;color:var(--ink);font-size:7px}
.canvas{position:relative;width:738px;height:1200px;overflow:hidden}
.abs{position:absolute}
.slab{font-family:"Bree Serif",Georgia,serif}

/* header */
.brand{left:87px;top:26px;font-family:"Bree Serif",serif;color:var(--red);font-size:22px;line-height:1;display:flex;align-items:center;gap:5px}
.brand-dot{width:10px;height:10px;background:var(--red)}
.brand-sub{left:118px;top:51px;font-family:"Bree Serif",serif;font-size:10px;color:#555}
.search-input{left:205px;top:38px;width:108px;height:17px;border:1px solid #ccc;border-radius:3px;font-size:7px;color:#999;padding:4px 7px}
.search-btn{left:316px;top:38px;width:53px;height:17px;background:linear-gradient(#ec2a2d,var(--red-dark));border-radius:3px;color:#fff;font-family:"Bree Serif",serif;font-size:8px;display:flex;align-items:center;justify-content:center;gap:3px}
.loc-label{left:384px;top:25px;font-size:7px;color:#333}
.loc-label a{color:var(--red);text-decoration:none}
.loc-field{left:382px;top:38px;width:70px;height:18px;border:1px solid #ccc;border-radius:3px;font-size:7px;text-align:center;line-height:16px}
.connect{left:475px;top:26px;font-size:8px}
.social{left:475px;top:40px;display:flex;gap:5px}
.social span{width:13px;height:13px;background:var(--red);border-radius:2px}
.phone{left:553px;top:38px;display:flex;align-items:center;gap:5px;font-family:"Bree Serif",serif;font-size:11px;color:#333}
.nav{left:87px;top:86px;width:563px;height:24px;background:linear-gradient(#e3201f,#b90f12);display:flex}
.nav a{flex:1;color:#fff;text-decoration:none;font-family:"Bree Serif",serif;font-size:8px;display:flex;align-items:center;justify-content:center;gap:3px;border-right:1px solid #a70c0f}
.nav a:last-child{border:none}
.caret{width:0;height:0;border:2px solid transparent;border-top:3px solid #fff;margin-top:3px}

/* slider */
.slider{left:87px;top:126px;width:389px;height:201px;border:3px solid #fff;box-shadow:0 0 3px rgba(0,0,0,.3)}
.slide-img{width:100%;height:100%;background:linear-gradient(120deg,#7a3f6e,#c07a5a 45%,#3b3c6a 80%,#1f2342)}
.caption{left:0;top:108px;width:337px;height:59px;background:rgba(0,0,0,.55);color:#fff;padding:8px 14px}
.caption h2{font-family:"Bree Serif",serif;font-weight:400;font-size:13px;margin-bottom:3px}
.caption p{font-size:7px;line-height:1.35}
.arrows{right:0;bottom:0;display:flex;gap:1px}
.arrows span{width:22px;height:23px;background:var(--red-dark);display:flex;align-items:center;justify-content:center}

/* side boxes */
.box{position:absolute;left:483px;width:166px;background:#fff;box-shadow:0 0 3px rgba(0,0,0,.25)}
.box h3{font-family:"Bree Serif",serif;font-weight:400;font-size:12px;padding:9px 12px 8px;border-bottom:1px dashed var(--line)}
.box h3 em{font-style:normal;color:var(--red)}
.news-note{font-size:7px;color:#888;text-align:center;line-height:1.4;padding:8px 14px 6px}
.field{margin:6px 9px 0;height:19px;border:1px solid #ddd;font-size:7px;padding:5px 6px;color:#555}
.btn-red{background:linear-gradient(#ec2a2d,var(--red-dark));color:#fff;border-radius:3px;font-family:"Bree Serif",serif;font-size:8px;display:flex;align-items:center;justify-content:center}
.btn-gold{background:linear-gradient(#ffd45c,var(--gold-dark));color:#5a3300;border-radius:3px;font-family:"Bree Serif",serif;font-size:8px;display:flex;align-items:center;justify-content:center;gap:4px}
.plain-list{list-style:none;font-size:6.5px;line-height:13.5px;padding:8px 11px}
.arrow-list{list-style:none;font-size:6.5px;line-height:13.5px;padding:9px 11px}
.arrow-list li::before{content:"»";color:var(--gold-dark);margin-right:5px}
.more{position:absolute;right:11px;font-family:"Bree Serif",serif;font-size:8px;color:var(--red)}

/* theater */
.section-title{font-family:"Bree Serif",serif;font-size:12px;color:#333}
.card{position:absolute;top:370px;width:120px;height:167px;background:#fff;box-shadow:0 0 3px rgba(0,0,0,.25)}
.card h4{font-family:"Bree Serif",serif;font-weight:400;color:var(--red);font-size:12px;text-align:center;padding:9px 0 10px;border-bottom:1px dashed var(--line)}
.card-img{margin:6px 10px 0;height:83px}
.card p{font-size:6.5px;color:#666;line-height:1.3;padding:7px 10px 0}

/* events */
.events{left:87px;top:574px;width:389px;height:369px;background:#fff;box-shadow:0 0 3px rgba(0,0,0,.25)}
.events h3{position:absolute;left:13px;top:10px;font-family:"Bree Serif",serif;font-weight:400;font-size:12px}
.ev-head{position:absolute;left:0;top:34px;width:100%;height:21px;background:var(--cream);border-top:1px solid #f0c66a;color:var(--red);font-family:"Bree Serif",serif;font-size:7.5px}
.ev-head span{position:absolute;top:6px}
.ev-row{position:absolute;left:0;width:100%;height:43px;border-bottom:1px dashed #ccc;font-size:6.5px;line-height:1.35}
.ev-row div{position:absolute;top:8px}
.ev-row .btn-gold{position:absolute;top:11px;left:303px;width:77px;height:17px}
.view-all{position:absolute;top:356px;font-size:6.5px;line-height:1}
.view-all a{color:var(--red);text-decoration:none;position:absolute;white-space:nowrap}

/* footer */
.rule{left:89px;width:560px;border-top:1px dashed #999}
.foot-col h5{font-family:"Bree Serif",serif;font-weight:400;font-size:11px;margin-bottom:12px}
.copyright{left:0;top:1169px;width:738px;text-align:center;font-size:6.5px;line-height:1.45;color:#444}
</style>
</head>
<body>
<div class="canvas">

  <!-- header -->
  <div class="abs brand"><span class="brand-dot"></span>SeatLoft</div>
  <div class="abs brand-sub">Website</div>
  <div class="abs search-input">Search Event, Tickets...</div>
  <div class="abs search-btn">Search
    <svg width="8" height="8" viewBox="0 0 10 10"><circle cx="4" cy="4" r="3" fill="none" stroke="#fff" stroke-width="1.5"/><line x1="6.3" y1="6.3" x2="9" y2="9" stroke="#fff" stroke-width="1.5"/></svg>
  </div>
  <div class="abs loc-label">Your Location : <a>Edit</a></div>
  <div class="abs loc-field">Wahington</div>
  <div class="abs connect">Connect with us</div>
  <div class="abs social"><span></span><span></span><span></span></div>
  <div class="abs phone">
    <svg width="12" height="16" viewBox="0 0 12 16"><rect x="1" y="1" width="10" height="14" rx="1.5" fill="var(--red)"/><rect x="3" y="3" width="6" height="4" fill="#fff"/><rect x="3" y="9" width="2" height="2" fill="#fff"/><rect x="7" y="9" width="2" height="2" fill="#fff"/></svg>
    1-800-555-0142
  </div>

  <nav class="abs nav">
    <a>Home</a>
    <a>Upcoming <i class="caret"></i></a>
    <a>Sports <i class="caret"></i></a>
    <a>Concerts <i class="caret"></i></a>
    <a>Theater <i class="caret"></i></a>
    <a>Las Vegas <i class="caret"></i></a>
    <a>Location</a>
  </nav>

  <!-- slider -->
  <div class="abs slider">
    <div class="slide-img" role="img" aria-label="Photo of friends celebrating at a night event"></div>
    <div class="abs caption">
      <h2>Lorem ipsum dolor sit amet</h2>
      <p>Nam liber tempor cum soluta nobis eleifend option congue nihil imperdiet doming id quod mazim placerat facer possim assum.</p>
    </div>
    <div class="abs arrows">
      <span><svg width="6" height="8"><path d="M5 0L1 4l4 4" fill="none" stroke="#fff" stroke-width="1.6"/></svg></span>
      <span><svg width="6" height="8"><path d="M1 0l4 4-4 4" fill="none" stroke="#fff" stroke-width="1.6"/></svg></span>
    </div>
  </div>

  <!-- theater -->
  <div class="abs section-title" style="left:87px;top:342px">Featured Theater Tickets</div>
  <div class="card" style="left:88px">
    <h4>Starfall</h4>
    <div class="card-img" role="img" aria-label="Poster for the musical Starfall" style="background:linear-gradient(160deg,#d7e4c8,#5d8a3c 55%,#1f2b18)"></div>
    <p>Somewhere over the rainbow, you will find the smash hit musical Starfall</p>
  </div>
  <div class="card" style="left:221px">
    <h4>Quarry Lane</h4>
    <div class="card-img" role="img" aria-label="Poster for the musical Quarry Lane" style="background:linear-gradient(180deg,#f0d49a,#9a6a3e 45%,#7a1416)"></div>
    <p>Somewhere over the rainbow, you will find the smash hit musical Quarry</p>
  </div>
  <div class="card" style="left:354px">
    <h4>Paper Moon</h4>
    <div class="card-img" role="img" aria-label="Poster for the stage show Paper Moon" style="background:linear-gradient(160deg,#2c3b8f,#4d6cc2 50%,#7a3b8c)"></div>
    <p>Somewhere over the rainbow, you will find the smash hit musical Moon</p>
  </div>
  <div class="abs btn-gold" style="left:434px;top:547px;width:41px;height:18px">More</div>

  <!-- events -->
  <section class="abs events">
    <h3>Events In the next 60 days in your area</h3>
    <div class="btn-red" style="position:absolute;left:301px;top:9px;width:79px;height:17px">Change Location</div>
    <div class="ev-head">
      <span style="left:13px">EVENT</span>
      <span style="left:140px">DATE/TIME ▾</span>
      <span style="left:217px">VENUE/CITY</span>
    </div>
    <div class="ev-row" style="top:55px"><div style="left:12px;width:120px">Lanternlight - The Musical Tickets 7/15</div><div style="left:141px">7-15-2013<br>Monday<br>7:30 PM</div><div style="left:218px;width:80px">Ashcombe Theatre in New York, NY</div><span class="btn-gold">Find your seats ›</span></div>
    <div class="ev-row" style="top:98px"><div style="left:12px;width:120px">Fernhill Music Center Orchestra Tickets 7/15</div><div style="left:141px">7-15-2013<br>Monday<br>8:00 PM</div><div style="left:218px;width:82px">Fernhill Music Center in Lenox, MA</div><span class="btn-gold">Find your seats ›</span></div>
    <div class="ev-row" style="top:141px"><div style="left:12px;width:120px">Orla Venn Tickets 7/15</div><div style="left:141px">7-15-2013<br>Monday<br>7:30 PM</div><div style="left:218px;width:82px">Lakeside Music And Convention Brandt Auditorium</div><span class="btn-gold">Find your seats ›</span></div>
    <div class="ev-row" style="top:184px"><div style="left:12px;width:120px">Spectrum Works: Artist of Light Tickets 7/15</div><div style="left:141px">7-15-2013<br>Monday<br>7:00 PM</div><div style="left:218px;width:82px">Corner Row Stages: Stage 4 in New York, NY</div><span class="btn-gold">Find your seats ›</span></div>
    <div class="ev-row" style="top:227px"><div style="left:12px;width:122px">Summerfold Festival of Music: Cass Ridley, Tinroof &amp; Hollow Oak Tickets 7/15</div><div style="left:141px">7-15-2013<br>Monday<br>5:30 PM</div><div style="left:218px;width:82px">Bayline Amphitheatre in Toronto, ON</div><span class="btn-gold">Find your seats ›</span></div>
    <div class="ev-row" style="top:270px"><div style="left:12px;width:120px">The Quillfords Tickets 7/15</div><div style="left:141px">7-15-2013<br>Monday<br>7:30 PM</div><div style="left:218px;width:82px">The Alder Music Hall in Denver, CO</div><span class="btn-gold">Find your seats ›</span></div>
    <div class="ev-row" style="top:313px;border-bottom:1px solid #ccc"><div style="left:12px;width:120px">Stagecraft The Musical Tickets 7/15</div><div style="left:141px">7-15-2013<br>Monday<br>8:15 PM</div><div style="left:218px;width:82px">Thorne Theater in New York, NY</div><span class="btn-gold">Find your seats ›</span></div>
    <div class="view-all" style="left:12px">View All :</div>
    <div class="view-all" style="left:0;width:100%"><a style="left:122px">Sport Tickets</a><a style="left:187px">Concert Tickets</a><a style="left:261px">Theater Tickets</a><a style="left:334px">Other Tickets</a></div>
  </section>

  <!-- newsletter -->
  <aside class="box" style="top:128px;height:196px">
    <h3>Event Newsletter</h3>
    <p class="news-note">Free updates, discounts and hot events in your area, sent right to your email!</p>
    <div class="field">Full Name</div>
    <div class="field" style="margin-top:12px">Email Address:</div>
    <div class="field" style="margin-top:12px">Zip Code:</div>
    <div class="btn-red" style="margin:12px auto 0;width:94px;height:18px">Join The Newsletter</div>
  </aside>

  <!-- guarantee -->
  <aside class="box" style="top:332px;height:142px">
    <h3>Guaranteed, <em>period!</em></h3>
    <ul class="plain-list">
      <li>Customer Service</li><li>Valid &amp; Authentic Tickets</li><li>On-Time Delivery</li><li>Refund for Cancellations</li><li>Secure Transaction</li>
    </ul>
    <div class="btn-gold" style="position:absolute;left:11px;top:113px;width:62px;height:17px">Learn More</div>
    <svg class="abs" style="left:92px;top:52px" width="70" height="70" viewBox="0 0 70 70" aria-hidden="true">
      <circle cx="35" cy="35" r="34" fill="var(--gold)"/>
      <circle cx="35" cy="35" r="27" fill="#fff" stroke="var(--gold-dark)" stroke-width="1.5"/>
    </svg>
  </aside>

  <!-- testimonials -->
  <aside class="box" style="top:482px;height:123px">
    <h3>Testimonials</h3>
    <div class="abs slab" style="left:10px;top:38px;font-size:22px;color:#bbb;line-height:1">“</div>
    <p class="abs" style="left:30px;top:42px;width:115px;font-size:6.5px;line-height:1.35">Ut wisi enim ad minim veniam, quis nostrud exerci tation ullamcorper suscipit lobortis nisl ut aliquip ex ea commodo consequat.</p>
    <div class="abs slab" style="left:30px;top:87px;font-size:8px;color:var(--red)">Mara Ellison - Wahington</div>
    <div class="abs slab" style="left:138px;top:82px;font-size:22px;color:#bbb;line-height:1">”</div>
    <svg class="abs" style="left:119px;top:106px" width="36" height="10"><circle cx="5" cy="5" r="4" fill="var(--gold)"/><circle cx="17" cy="5" r="4" fill="#fff" stroke="#bbb"/><circle cx="29" cy="5" r="4" fill="#fff" stroke="#bbb"/></svg>
  </aside>

  <!-- sports -->
  <aside class="box" style="top:613px;height:152px">
    <h3>Featured Sports Tickets</h3>
    <ul class="arrow-list">
      <li>Harbor Hawks tickets</li><li>Coastline Rays tickets</li><li>Prairie Stags tickets</li><li>Rico Delgado Jr tickets</li><li>Pro Ball All Star Game tickets</li><li>Lakeport Otters tickets</li><li>Bay City Foxes tickets</li>
    </ul>
    <span class="more" style="top:135px">More</span>
  </aside>

  <!-- concerts -->
  <aside class="box" style="top:773px;height:168px">
    <h3>Featured Concert Tickets</h3>
    <ul class="arrow-list">
      <li>Open Road Tour tickets</li><li>Milo Hartwell tickets</li><li>Corey Lindqvist tickets</li><li>Wade Callum tickets</li><li>Northbound Five tickets</li><li>Juno Marsh tickets</li><li>Elena Voss tickets</li>
    </ul>
    <span class="more" style="top:148px">More</span>
  </aside>

  <!-- footer -->
  <div class="abs rule" style="top:980px"></div>
  <div class="abs foot-col" style="left:110px;top:1011px"><h5>Browse Tickets</h5>
    <ul class="arrow-list" style="padding:0">
      <li>Open Road Tour tickets</li><li>Milo Hartwell tickets</li><li>Corey Lindqvist tickets</li><li>Wade Callum tickets</li><li>Northbound Five tickets</li><li>Juno Marsh tickets</li><li>Elena Voss tickets</li>
    </ul></div>
  <div class="abs foot-col" style="left:252px;top:1011px"><h5>City Guides</h5>
    <ul class="arrow-list" style="padding:0">
      <li>chicago city guide</li><li>miami city guide</li><li>new york city guide</li><li>boston city guide</li><li>san diego tickets</li><li>all city guides</li>
    </ul></div>
  <div class="abs foot-col" style="left:374px;top:1011px"><h5>Help &amp; Support</h5>
    <ul class="arrow-list" style="padding:0">
      <li>about us</li><li>guarantee</li><li>faq</li><li>send feedback</li><li>contact us</li>
    </ul></div>
  <div class="abs foot-col" style="left:514px;top:1011px"><h5>Popular Events</h5>
    <ul class="arrow-list" style="padding:0">
      <li>pro football tickets</li><li>pro basketball tickets</li><li>pro baseball tickets</li><li>pro hockey tickets</li><li>pro golf tickets</li>
    </ul></div>
  <div class="abs rule" style="top:1152px"></div>
  <div class="abs copyright">About Us | Contact Us | Link to Us | Phone: 1.555.0199.731<br>Copyright © 2008-2013 seatloft.com. All Rights Reserved. | Privacy Policy | Terms of Use</div>

</div>
</body>
</html>
```